Movie poster for drama/thriller feature

We need a movie poster for an edgy microbudget, drama/thriller feature called Stumbling My Road Past Dawn and is about a “night in the life” of an escort and her driver after she discovers that her mother, who was caring for her daughter, has died. She has just one night to raise the money to cover the arrears on her mother’s mortgage and return to collect her daughter before her very religious aunt calls Children’s Aid. On top of that she has to enlist the help of her new driver who is also very religious and hates her because she’s a “whore”. He is only doing this job because, as a Cuban refugee, he has had to take a job with his uncle, who is head of security at the agency, in order to pay him back what it cost to bring him to Canada. So, at the core of the story is this relationship between two people who hate each other but are stuck together in a car for an entire night. The third character is the uncle - head of security - who becomes increasingly "dark" and violent as the night goes on as he feels he is losing the loyalty of his nephew to a sex worker who is ripping off his boss.

So, that's the backdrop to the story.

Now, we want the poster to reflect that this is a scrappy, edgy little film, a bit controversial (just the title alone, obviously). Some of our inspiration for the poster are the kind of minimalist designs from French New Wave films (examples uploaded). The title itself can either be written out in toto or you could put the acronym in bold letters - SMRPD - with their meaning smaller below it. You can play with it, anyway, to come up with some cool. I've also included stills from the film of the three main characters - Marisol, the lead/star, Tomas (her driver) and Ignacio, the antaonist/uncle. You can crop these to make them work. I just left them full size so that you'd have more options.

If you have questions, don't hesitate to ask.

best
Derek

Target Market(s)

indie film goers, younger, city-based, hipster demographic

Industry/Entity Type

Film Production

Font styles to use
Sans Serif

Colors

Designer to choose colors to be used in the design.

Requirements
Must have
• A great look, the title, and some credits:
• tagline: one night can change your whole world
• A film by Bridget Oldcastle & Derek Fenwold
• With
• Ingrid Tolmachova
• Esteban Morales-Quiroga
• Raul Caceres Villalobos
• Cinematography
• Nate Corbell
• Produced by:
• Crooked Lantern Productions
• Pinecrest Studios
• and a credit block with:
• Bridget Oldcastle ... co-producer
• Ingrid Tolmachova ... co-producer
• Esteban Morales-Quiroga ... co-producer
• Gavin Trout ... co-producer
• Derek Fenwold ... co-producer
• Editing by
• Dana McGivney
• Production Design by
• Tiago Mendes Rocha
• Wendy Calder ... key makeup artist
• Priscilla Novak ... makeup artist Production Management
• Tessa Kimball ... production manager Second Unit Director or Assistant Director
• Tessa Kimball ... first assistant director Sound Department
• Ben Yardley ... sound editor
• Kevin Santoso ... sound recordist Stunts
• Raul Caceres Villalobos ... action coordinator
• Carl Pembry ... still photographer
• Fiona Beckett ... swing
• Monica Thorne ... still photographer
• Giulia Marchetti ... swing Costume and Wardrobe Department
• Nora Fairclough ... wardrobe
• Petra Holub ... wardrobe supervisor Transportation Department
• Rosalind Tapley ... craft service
• Maya Finch ... script supervisor
• Paolo Reyes ... production assistant
• Lucia Navarro ... craft service

```html
<!DOCTYPE html>
<html lang="en">
<head>
<meta charset="utf-8">
<title>Stumbling My Road Past Dawn — Poster</title>
<link href="https://fonts.googleapis.com/css2?family=Anton&family=Antonio:wght@100;300;400&display=swap" rel="stylesheet">
<style>
  :root {
    --paper: #ffffff;
    --ink: #111111;
    --uncle-green: #2e5b3a;
    --lead-magenta: #a32f72;
    --driver-maroon: #561b1e;
    --photo-dark: #2b2b2b;
    --photo-mid: #7a7a7a;
    --photo-light: #bdbdbd;
  }
  html, body { margin: 0; padding: 0; overflow: hidden; background: var(--paper); }
  .poster {
    position: relative; width: 849px; height: 1200px; overflow: hidden;
    background: var(--paper); color: var(--ink);
    font-family: "Antonio", "Oswald", sans-serif;
  }
  .directed-by {
    position: absolute; top: 22px; left: 0; width: 100%;
    text-align: center; font-weight: 400; font-size: 29px; letter-spacing: 3.2px;
    margin: 0;
  }
  .cast-name {
    position: absolute; margin: 0; font-weight: 400; font-size: 21px; letter-spacing: 2.4px;
    text-align: center; white-space: nowrap;
  }
  .cast-name--uncle { top: 78px; left: 309px; width: 241px; color: var(--uncle-green); }
  .cast-name--lead { top: 620px; left: 54px; width: 241px; color: var(--lead-magenta); font-size: 20px; letter-spacing: 1.6px; }
  .cast-name--driver { top: 620px; left: 564px; width: 241px; color: var(--driver-maroon); font-size: 20px; letter-spacing: 1.2px; }
  .still { position: absolute; width: 241px; height: 239px; }
  .still--uncle { top: 115px; left: 309px; background: linear-gradient(160deg, var(--photo-dark) 0%, #4a4a4a 45%, var(--photo-mid) 75%, #3a3a3a 100%); }
  .still--lead { top: 370px; left: 54px; background: linear-gradient(100deg, #1e1e1e 0%, var(--photo-mid) 40%, var(--photo-light) 60%, #555 100%); }
  .still--driver { top: 370px; left: 564px; background: linear-gradient(200deg, #1a1a1a 0%, #3d3d3d 50%, var(--photo-mid) 85%, #4a4a4a 100%); }
  .title-stack { position: absolute; top: 370px; left: 309px; width: 241px; height: 740px; }
  .title-stack .title-line { font-family: "Anton", "Impact", sans-serif; fill: var(--ink); }
  .title-stack .tagline-line { font-family: "Antonio", sans-serif; font-weight: 100; fill: var(--ink); }
  .credit-side { position: absolute; top: 1043px; margin: 0; line-height: 1; text-transform: uppercase; }
  .credit-side .role { display: block; font-size: 13px; font-weight: 400; letter-spacing: -0.2px; margin-bottom: 6px; }
  .credit-side .who { display: block; font-size: 19px; font-weight: 300; line-height: 22px; }
  .credit-side--camera { left: 54px; }
  .credit-side--producers { right: 44px; text-align: right; }
  .billing-block { position: absolute; top: 1120px; left: 0; width: 849px; height: 80px; }
  .billing-block text { font-family: "Antonio", sans-serif; fill: var(--ink); font-weight: 400; font-size: 11px; }
  .billing-block .label { font-size: 5.5px; }
</style>
</head>
<body>
<main class="poster">
  <p class="directed-by">A FILM BY BRIDGET OLDCASTLE &amp; DEREK FENWOLD</p>

  <p class="cast-name cast-name--uncle">RAUL CACERES VILLALOBOS</p>
  <div class="still still--uncle" role="img" aria-label="Black and white still of Ignacio, the uncle, in a flat cap and patterned shirt"></div>

  <div class="still still--lead" role="img" aria-label="Black and white still of Marisol seated in a car at night, lips in magenta"></div>
  <div class="still still--driver" role="img" aria-label="Black and white still of Tomas at the wheel, a red cross hanging from the mirror"></div>
  <p class="cast-name cast-name--lead">INGRID TOLMACHOVA</p>
  <p class="cast-name cast-name--driver">ESTEBAN MORALES-QUIROGA</p>

  <svg class="title-stack" viewBox="0 0 241 740" aria-label="Stumbling My Road Past Dawn — one night can change your whole world">
    <text class="title-line" x="0" y="95" font-size="120" textLength="241" lengthAdjust="spacingAndGlyphs">STUMBLING</text>
    <text class="title-line" x="0" y="226" font-size="120" textLength="241" lengthAdjust="spacingAndGlyphs">MY ROAD</text>
    <text class="title-line" x="0" y="357" font-size="120" textLength="241" lengthAdjust="spacingAndGlyphs">PAST</text>
    <text class="title-line" x="0" y="512" font-size="170" textLength="241" lengthAdjust="spacingAndGlyphs">DAWN</text>
    <text class="tagline-line" x="0" y="597" font-size="62" textLength="241" lengthAdjust="spacingAndGlyphs">ONE NIGHT CAN</text>
    <text class="tagline-line" x="0" y="664" font-size="62" textLength="241" lengthAdjust="spacingAndGlyphs">CHANGE YOUR</text>
    <text class="tagline-line" x="0" y="731" font-size="62" textLength="241" lengthAdjust="spacingAndGlyphs">WHOLE WORLD</text>
  </svg>

  <p class="credit-side credit-side--camera">
    <span class="role">Cinematography</span>
    <span class="who">Nate<br>Corbell</span>
  </p>
  <p class="credit-side credit-side--producers">
    <span class="role">Produced by</span>
    <span class="who">Crooked Lantern Productions<br>Pinecrest Studios</span>
  </p>

  <svg class="billing-block" viewBox="0 0 849 80" aria-label="Full crew credits">
    <text x="54" y="13" textLength="751" lengthAdjust="spacingAndGlyphs"><tspan class="label">CO-PRODUCERS </tspan>BRIDGET OLDCASTLE, INGRID TOLMACHOVA, ESTEBAN MORALES-QUIROGA, GAVIN TROUT, DEREK FENWOLD. <tspan class="label">EDITING BY </tspan>DANA MCGIVNEY. <tspan class="label">PRODUCTION DESIGN BY </tspan>TIAGO MENDES ROCHA. <tspan class="label">KEY MAKEUP ARTIST </tspan>WENDY CALDER.</text>
    <text x="54" y="31" textLength="751" lengthAdjust="spacingAndGlyphs"><tspan class="label">MAKEUP ARTIST PRODUCTION MANAGEMENT </tspan>PRISCILLA NOVAK. <tspan class="label">PRODUCTION MANAGER SECOND UNIT DIRECTOR OR ASSISTANT DIRECTOR </tspan>TESSA KIMBALL. <tspan class="label">FIRST ASSISTANT DIRECTOR SOUND DEPARTMENT </tspan>TESSA KIMBALL. <tspan class="label">SOUND EDITOR </tspan>BEN YARDLEY. <tspan class="label">SOUND RECORDIST STUNTS </tspan>KEVIN SANTOSO.</text>
    <text x="54" y="49" textLength="751" lengthAdjust="spacingAndGlyphs"><tspan class="label">ACTION COORDINATOR </tspan>RAUL CACERES VILLALOBOS. <tspan class="label">STILL PHOTOGRAPHERS </tspan>CARL PEMBRY, MONICA THORNE. <tspan class="label">SWING </tspan>FIONA BECKETT. <tspan class="label">SWING COSTUME AND WARDROBE DEPARTMENT </tspan>GIULIA MARCHETTI. <tspan class="label">WARDROBE </tspan>NORA FAIRCLOUGH. <tspan class="label">WARDROBE SUPERVISOR</tspan></text>
    <text x="158" y="67" textLength="542" lengthAdjust="spacingAndGlyphs"><tspan class="label">TRANSPORTATION DEPARTMENT </tspan>PETRA HOLUB. <tspan class="label">CRAFT SERVICE </tspan>ROSALIND TAPLEY. <tspan class="label">SCRIPT SUPERVISOR </tspan>MAYA FINCH. PRO<tspan class="label">DUCTION ASSISTANT </tspan>PAOLO REYES. <tspan class="label">CRAFT SERVICE </tspan>LUCIA NAVARRO.</text>
  </svg>
</main>
</body>
</html>
```